This book will apply the 12 Steps to gaming addiction, also known as video game addiction. The primary purpose of the book is to provide an effective solution for this new type of addiction. The solution is based on the rich and successful concepts of traditional twelve-step programs like RL.

The title on the cover will be "Nine Doors Past the Glowing Screen" and "by Martin Quorby". A subtitle can be used if it works in your design of "A Practical Path Beyond Compulsive Console Play". Cover will be for a 6" x 9" book approximately 110 pages in length.

Some back cover text including some review quotes and an author bio are in the attached Word doc. There is also an author photo attached for for the back cover.

Requirements
Must have
• For the cover design it could be stylized, or an image, a partial image, or whatever. I am open to suggestions. Think about what would be noticed by a person searching for help with moderating their video game use, or by the parents or loved ones of problem gamers. Something contemporary and eye catching.

```html
<!DOCTYPE html>
<html lang="en">
<head>
<meta charset="utf-8">
<title>Nine Doors Past the Glowing Screen – Back Cover</title>
<link rel="stylesheet" href="https://fonts.googleapis.com/css2?family=Cinzel:wght@400;500&display=swap">
<style>
  :root {
    --backdrop-light: #8a8a8a;
    --backdrop-dark: #4e4e4e;
    --panel: #2b2b2b;
    --panel-edge: #232323;
    --photo-light: #9a9a9a;
    --photo-dark: #2e2e2e;
    --ink: #f2f2f2;
  }
  * { margin: 0; padding: 0; box-sizing: border-box; }
  html, body { width: 800px; height: 1200px; overflow: hidden; }
  body {
    position: relative;
    background: radial-gradient(ellipse at 50% 45%, var(--backdrop-light) 0%, #6d6d6d 55%, var(--backdrop-dark) 100%);
    font-family: "Cinzel", "Times New Roman", serif;
    color: var(--ink);
  }
  .back-cover-panel {
    position: absolute;
    left: 41px; top: 59px;
    width: 718px; height: 1085px;
    background: radial-gradient(ellipse at 50% 40%, #303030 0%, var(--panel) 60%, var(--panel-edge) 100%);
  }
  .author-photo {
    position: absolute;
    left: 244px; top: 159px;
    width: 230px; height: 208px;
    background: radial-gradient(ellipse at 50% 35%, var(--photo-light) 0%, #5e5e5e 45%, var(--photo-dark) 100%);
  }
  .cover-copy {
    position: absolute;
    left: 36px; top: 425px;
    width: 646px;
    text-align: center;
    text-transform: uppercase;
    font-size: 12.2px;
    line-height: 15.4px;
    letter-spacing: 0.15px;
  }
  .cover-copy p { margin-bottom: 0; }
  .review-quote { margin-bottom: 0; }
  .review-credit { }
  .pitch { margin-bottom: 27px; }
  .overview { margin-bottom: 28px; }
  .method { margin-bottom: 62px; }
  .bio-heading { margin-bottom: 27px; }
</style>
</head>
<body>
  <main class="back-cover-panel">
    <div class="author-photo" role="img" aria-label="Black and white portrait of author Martin Quorby smiling, in a dark jacket and open-collar shirt"></div>

    <section class="cover-copy">
      <p class="review-quote">“A must-read for anyone who is addicted to or thinks they may have a problem with digital gaming. This eloquent work will also be useful to academics and clinicians exploring potential solutions. The author recognizes the similarities between gaming addiction and other addictions, and logically applies one of the most effective known solutions for addiction – the twelve steps.”</p>
      <p class="review-credit">– Dale Winthorpe, noted interventionist and keynote speaker</p>
      <p class="pitch">An effective solution to the challenge of digital gaming addiction (aka video game addiction) based on the rich and successful tradition of the twelve steps.</p>

      <p class="overview">Addiction to digital gaming is a new and troubling phenomenon that has burst upon an unprepared society with alarming speed. Many people crave the use of digital games in a strikingly similar way to any other addict. Digital games are a complex software and hardware system that have been designed to promote continued and progressive usage. This sophisticated technology clearly feeds on natural addictive tendencies.</p>

      <p class="method">The 12 steps are one of the most effective methods for treating addiction in human history. Originating with Recovery League in 1939, the 12 steps have since been used to treat a variety of other addictions, including drugs, sex, gambling, eating disorders, and many others. Now in this groundbreaking work the 12 steps are applied to the complex and evolving contemporary phenomenon of digital gaming addiction.</p>

      <h2 class="bio-heading" style="font: inherit;">About the Author</h2>
      <p class="author-bio">Martin Quorby is a technology consultant and writer, with many years of professional coding and consulting experience. He also struggled with addiction to drugs and alcohol and is now clean and sober in a twelve-step program for over 17 years. This unique combination of 12-step experience and technology expertise led him to create Nine Doors Past the Glowing Screen.</p>
    </section>
  </main>
</body>
</html>
```